Solace Chiropractic & Acupuncture Business Cards

I need a business card design that feels elevated. I am open to any of the logo designs uploaded. We have two doctors so I'll need to be able to change out the names.

Information:
Marnie Toller D.C., Dipl. Ac. ASA
584 W 12th St, Ste 320
Hutchinson, KS 67419
solacegrove.net
620-555-0147
drmarnie@solacegrove.com
Updates

We have designs we like now, we are just trying to choose between top contenders. Thanks for your submissions!

Contact Information for Business Card

noted in description

Requirements
Must have
• ability to edit info if possible
Nice to have
• Please see our website solacegrove.net for our style and colors

```html
<!DOCTYPE html>
<html lang="en">
<head>
<meta charset="utf-8">
<title>Solace Chiropractic &amp; Acupuncture — Business Cards</title>
<link href="https://fonts.googleapis.com/css2?family=Playfair+Display:wght@400&family=Roboto:wght@400&family=Montserrat:wght@500&display=swap" rel="stylesheet">
<style>
  :root {
    --backdrop: #232323;
    --paper: #efefef;
    --navy: #3e4256;
    --sand: #cdc7bb;
    --ink: #3a3d50;
    --muted: #6a6c78;
    --icon: #b4b1aa;
  }
  html, body {
    margin: 0;
    padding: 0;
    width: 1200px;
    height: 576px;
    overflow: hidden;
    background: var(--backdrop);
  }
  .stage { position: relative; width: 1200px; height: 576px; }
  .card {
    position: absolute;
    top: 138px;
    width: 484px;
    height: 293px;
    background: var(--paper);
    border-radius: 8px;
    overflow: hidden;
  }
  .card--front { left: 102px; }
  .card--back { left: 596px; width: 480px; }

  .wordmark {
    position: absolute;
    left: 0; right: 0;
    top: 58px;
    text-align: center;
    color: var(--ink);
    font-family: "Playfair Display", serif;
    font-weight: 400;
  }
  .wordmark__name { display: block; font-size: 84px; line-height: 1; letter-spacing: -1px; }
  .wordmark__sub { display: block; font-size: 13px; letter-spacing: 0.5px; margin-top: 6px; padding-left: 70px; text-transform: uppercase; }

  .web-band {
    position: absolute;
    left: 0; right: 0;
    top: 237px;
    height: 34px;
    background: var(--sand);
    display: flex;
    align-items: center;
    justify-content: center;
    font-family: "Montserrat", sans-serif;
    font-weight: 500;
    font-size: 12px;
    letter-spacing: 3px;
    color: var(--ink);
  }

  .panel { position: absolute; left: 0; top: 0; }

  .brand {
    position: absolute;
    left: 36px;
    width: 160px;
    top: 62px;
    text-align: center;
    color: var(--sand);
    font-family: "Playfair Display", serif;
    font-weight: 400;
  }
  .brand__mark {
    width: 70px; height: 70px;
    margin: 0 auto 16px;
    border: 1px solid var(--sand);
    border-radius: 50%;
  }
  .brand__name { display: block; font-size: 22px; letter-spacing: 3px; text-transform: uppercase; }
  .brand__sub { display: block; font-size: 12px; line-height: 1.35; text-transform: uppercase; margin-top: 6px; }

  .contact {
    position: absolute;
    left: 278px;
    top: 68px;
    font-family: "Roboto", sans-serif;
    color: var(--muted);
    font-size: 12px;
  }
  .contact__name {
    font-family: "Playfair Display", serif;
    color: var(--ink);
    font-size: 22px;
    line-height: 1;
    margin: 0;
    font-weight: 400;
  }
  .contact__creds { margin: 4px 0 0; font-size: 11.5px; }
  .contact__address { margin: 26px 0 6px; line-height: 17.5px; font-style: normal; }
  .contact__list { list-style: none; margin: 0; padding: 0; }
  .contact__item { display: flex; align-items: center; gap: 10px; height: 17.5px; }
  .contact__item svg { width: 9px; height: 9px; fill: none; stroke: var(--icon); stroke-width: 1.6; }
</style>
</head>
<body>
<main class="stage">

  <section class="card card--front" aria-label="Card front">
    <div class="wordmark">
      <span class="wordmark__name">Solace</span>
      <span class="wordmark__sub">Chiropractic &amp; Acupuncture</span>
    </div>
    <div class="web-band">www.solacegrove.net</div>
  </section>

  <section class="card card--back" aria-label="Card back">
    <svg class="panel" width="480" height="293" viewBox="0 0 480 293" aria-hidden="true">
      <path d="M0 0 H196 Q 282 140 204 293 H0 Z" fill="var(--sand)"/>
      <path d="M0 0 H188 Q 270 140 186 293 H0 Z" fill="var(--navy)"/>
    </svg>

    <div class="brand">
      <div class="brand__mark"></div>
      <span class="brand__name">Solace</span>
      <span class="brand__sub">Chiropractic<br>&amp; Acupuncture</span>
    </div>

    <div class="contact">
      <h1 class="contact__name">Dr. Marnie Toller</h1>
      <p class="contact__creds">D.C., Dipl. Ac. ASA</p>
      <address class="contact__address">584 W 12th St, Ste 320<br>Hutchinson, KS 67419</address>
      <ul class="contact__list">
        <li class="contact__item">
          <svg viewBox="0 0 10 10"><path d="M2 1 L4 3 L3 4.5 Q4.5 6.5 5.5 7 L7 6 L9 8 L7.5 9.2 Q3 8 0.8 2.5 Z" fill="var(--icon)" stroke="none"/></svg>
          620-555-0147
        </li>
        <li class="contact__item">
          <svg viewBox="0 0 10 10"><circle cx="5" cy="5" r="1.8"/><path d="M6.8 5 V6 Q6.8 7.5 8 7.5 Q9 7.5 9 5 A4 4 0 1 0 7 8.5"/></svg>
          drmarnie@solacegrove.com
        </li>
        <li class="contact__item">
          <svg viewBox="0 0 10 10"><circle cx="5" cy="5" r="4"/><path d="M1 5 H9 M5 1 Q2.5 5 5 9 M5 1 Q7.5 5 5 9"/></svg>
          www.solacegrove.net
        </li>
      </ul>
    </div>
  </section>

</main>
</body>
</html>
```